Zestra Design Prize - $10,000 tablet app design contest, Magazine Category

Zestra is a marketplace for uSlate App Templates (similar to PageLoom templates). We want you to design an app template for sale in our marketplace which targets B2B or B2C Magazine Apps (uSlate Apps created for examples such as Alumni magazine, employee magazine, sports magazine, fashion magazine etc).

It’s up to you to create pages or features for the App Template that you think are appropriate. Creativity will be rewarded! Here are some example pages or features that you could create:

• Contents
• Editor’s letter
• Event calendar
• News page
• Feature article
• Business articles
• Social media integration
• Animations and video

Your design should be Vibrant, Engaging and Contemporary. If you have an uSlate, download Zestra Viewer and download template examples in the download tab.

Your entry must include:
• A brief description of your template
• Preview images of all pages of your template

Attached to this project are free templates to help you get started with your design. We have included:
1. A free portfolio template for designers/photographers
2. Icons and artwork to use in your template
3. Blank pages template
4. Form template
5. Video ad template

If you are selected as a finalist you will be required to submit an .oproject file containing:
• Your LayoutCraft source files
• Preview images of your template
• All creative / stock assets used in the template (animations, video etc.)
• A text file with instructions on how to update the template
• A metadata .txt file containing template details and your information

How to enter:
1. Register at Marketplace and view the instructions under the welcome message https://marketplace.zestrahub.test/welcome
2. Download Zestra Editor: https://support.zestrahub.test/entries/58104926-zestra-editor
3. Use the free templates provided in this brief to create your designs and submit to ArtFlock
Updates

Reason: Due to the Christmas break we are extending the deadline of our competition. Thank you for time and effort - I will be providing feedback over the next couple of days! Best wishes, Melody

Hi All,

I have received many screenshots with some great designs! I just wanted to clarify that you are designing Zestra app templates including Zestra features and not just page designs?

Read Tips for First Time Zestrans to guide you through the template creation process

Before you start designing templates for Zestra Marketplace

·       Read the Quality Standards

·       Read the Copyright Information 

·       Use the Template Quality Checklist to ensure your template follows our guidelines. 

What should my project file contain?

·       A folder containing your source files, e.g. LayoutCraft. This must be named Source.

·       The Zestra content files. This must be named Bundle.

·       Instructions, explaining to a customer how to use your template.

Best wishes,

Melody

Reason: We are extending the competition by 7 days to give you more time!

Reason: We have received 3 complete designs for this contest so we are extending the deadline for 7 days Best wishes, Melody

Target Market(s)

Entrepreneurs who wish to create uSlate Apps by using our App design templates.

Industry/Entity Type

Fashion

Requirements
Must have
• You will need Zestra Editor to open the .oproject files attached to this brief. Get it here: https://support.zestrahub.test/entries/58104926-zestra-editor
Should not have
• • Low quality, fuzzy or blurry images
• Any stock images or content which you do not own the rights to
• Any material which could be considered inappropriate or offensive

```html
<!DOCTYPE html>
<html lang="en">
<head>
<meta charset="utf-8">
<title>Page no 9 – Interiors</title>
<link rel="stylesheet" href="https://fonts.googleapis.com/css2?family=Arimo:ital@0;1&family=EB+Garamond:wght@400;700&display=swap">
<style>
  :root {
    --paper: #ffffff;
    --frame: #2a2a2a;
    --title-grey: #6a6a6a;
    --tagline: #6b2416;
    --bullet-red: #e30d0d;
    --brand-orange: #d24a19;
    --blush: #edd0cf;
    --cell-gap: #ffffff;
    --ink-dark: #1a1a1a;
    --room-wall: #c9cf9a;
    --room-floor: #d9b98a;
  }
  * { box-sizing: border-box; margin: 0; padding: 0; }
  html, body {
    width: 1200px; height: 900px; overflow: hidden;
    background: var(--paper);
  }
  .slide {
    position: relative; width: 1200px; height: 900px;
    background: var(--paper);
  }
  .slide-frame {
    position: absolute; left: 10px; top: 10px; width: 1180px; height: 876px;
    border: 2px solid var(--frame); border-radius: 48px;
    box-shadow: 2px 3px 0 var(--frame);
  }
  .page-title {
    position: absolute; left: 132px; top: 60px;
    font-family: "Arimo", Arial, sans-serif; font-weight: 400;
    font-size: 50px; color: var(--title-grey); letter-spacing: 0.5px;
  }
  .page-tagline {
    position: absolute; left: 133px; top: 134px;
    font-family: "Arimo", Arial, sans-serif; font-style: italic;
    font-size: 32px; color: var(--tagline); white-space: nowrap;
  }
  .room-photo {
    position: absolute; left: 669px; top: 100px; width: 422px; height: 490px;
    background: linear-gradient(180deg, var(--room-wall) 0%, #d6d9a8 60%, var(--room-floor) 82%, #8fb6d6 100%);
  }
  .section-heading {
    position: absolute; left: 136px; top: 202px;
    font-family: "EB Garamond", Garamond, serif; font-weight: 400;
    font-size: 62px; color: var(--bullet-red); line-height: 1;
    display: flex; align-items: center; gap: 6px;
    background: var(--paper); padding-right: 6px;
  }
  .section-heading::before {
    content: ""; width: 24px; height: 24px; border-radius: 50%;
    background: var(--ink-dark); margin-top: 4px;
  }
  .brand-grid {
    position: absolute; left: 2px; top: 270px; width: 798px; height: 598px;
    display: grid;
    grid-template-columns: 198px 99px 97px 398px;
    grid-template-rows: 296px 296px;
    gap: 3px;
    background: var(--cell-gap);
    font-family: "EB Garamond", Garamond, serif;
    font-size: 24px; line-height: 36px;
  }
  .brand-cell {
    padding: 10px 4px 10px 13px;
    text-transform: uppercase;
    word-break: normal;
    overflow-wrap: normal;
  }
  .brand-cell--lead { grid-row: 1 / 3; }
  .brand-cell--featured {
    background: var(--brand-orange); color: var(--paper); font-weight: 700;
  }
  .brand-cell--listed {
    background: var(--blush); color: var(--ink-dark); font-weight: 400;
  }
</style>
</head>
<body>
  <main class="slide">
    <div class="slide-frame"></div>
    <h1 class="page-title">Page no&nbsp; 9:</h1>
    <div class="room-photo" role="img" aria-label="Photo of a bright children's room with white cube shelving, coloured storage bins, toys and a patchwork floor rug"></div>
    <p class="page-tagline">concealed talent brings no reputation</p>
    <h2 class="section-heading">Interiors:</h2>
    <section class="brand-grid" aria-label="Interior brands">
      <div class="brand-cell brand-cell--lead brand-cell--featured">Build a house in Jannah:</div>
      <div class="brand-cell brand-cell--featured">Poise and Ease</div>
      <div class="brand-cell brand-cell--featured">Oak Lane</div>
      <div class="brand-cell brand-cell--featured">Vellacasa</div>
      <div class="brand-cell brand-cell--listed">Nook and Nest</div>
      <div class="brand-cell brand-cell--listed">Clay and Line</div>
      <div class="brand-cell brand-cell--listed">Hearth Grace</div>
    </section>
  </main>
</body>
</html>
```